Give Tall Oak Ridge an Online Presence!

Tall Oak Ridge Property Maintenance is an Australian Owned property maintenance company who needs a stand out online presence.

TOR maintains many buildings and sites and wants to appeal to a corporate professional market with their brand new website. TOR is essentially a handyman service offering all maintenance services to home owners, office managers, real estate agents and strata managers.

The Website:
We need a corporate website that appeals to our broader customer base (property owners, property managers, office managers) the copy is being written by a professional so use filler text for now.

Things that we want:
Home page that sets us apart and appeals to the corporate and residential market. The home page needs to not focus on either the residential or commercial market. The home page should focus on our logo and branding. We have a logo already and it is attached to the brief, please use it and try to consider the colour pallette that goes with it. Whilst we want the site to appear strong and manly it is important to remember that 95% of our customers are female so we need the site to be appealing to women. Women need to believe that we are strong, dependable and trustworthy.
We'd like a quote page and potentially also the ability to get a quote from the home page (please don't put it in if it ruins the overall feel of the home page)
An "about us" page
A contact us page
A blog that's built in (we don't want to link to an external blog)
(overall we'd expect to have 6 or 7 pages total)

The site will also need coding - we expect this to be done in a separate project but need you to consider a few things about the coding side of things.

It needs to be iPhone and iPad compatible.

We'd like you to suggest the best CMS that you would use or if you would suggest not using a CMS please let us know with your submissions.

Target Market(s)

Property owners, office managers and property managers who need maintenance on buildings (So all of them)

Industry/Entity Type

Property Maintenance

Requirements
Must have
• Our Logo
Home page
About Us
Residential
Commercial
Real Estate/Strata
Contact Us/Quote
Blog
Nice to have
• Quote form included in home page
Movement on the home page at least
Should not have
• other logos, too much colour
NO FLASH

```html
<!DOCTYPE html>
<html lang="en">
<head>
<meta charset="utf-8">
<title>Tall Oak Ridge Property Maintenance – Contact Us / Get a Quote</title>
<link rel="stylesheet" href="https://fonts.googleapis.com/css2?family=Montserrat:wght@500;700&family=Roboto+Condensed:ital,wght@0,700;1,400&family=Arimo:wght@400;700&display=swap">
<style>
:root{
  --orange:#f47a12;
  --orange-deep:#ef5f06;
  --orange-glow:#f9b21c;
  --ink:#111;
  --nav-top:#3a3a3a;
  --nav-bottom:#050505;
  --text:#444;
  --heading:#222;
  --muted:#555;
  --rule:#c9c9c9;
  --field-border:#b9b9b9;
  --white:#fff;
}
*{box-sizing:border-box;margin:0;padding:0}
html,body{width:1200px;height:1156px;overflow:hidden}
body{position:relative;background:var(--white);font-family:"Arimo",Arial,sans-serif;color:var(--text)}
.abs{position:absolute}

/* top navigation */
.top-nav{position:absolute;left:0;top:0;width:1200px;height:46px;background:linear-gradient(var(--nav-top),var(--nav-bottom))}
.top-nav ul{list-style:none;position:absolute;left:125px;top:0;display:flex;height:46px;border-left:1px solid #444}
.top-nav li{height:46px;border-right:1px solid #444;display:flex;align-items:center;justify-content:center;font-family:"Roboto Condensed",sans-serif;font-weight:700;font-size:11px;color:var(--white);text-transform:uppercase}
.search-box{position:absolute;left:917px;top:10px;width:187px;height:23px;border-radius:5px;background:linear-gradient(#1a1a1a,#2f2f2f);border:1px solid #555;color:#aaa;font-size:10px;padding:5px 22px 0 0;text-align:right}
.search-box svg{position:absolute;left:12px;top:4px}

/* hero */
.hero{position:absolute;left:0;top:46px;width:1200px;height:298px;background:linear-gradient(180deg,var(--orange-deep),var(--orange) 55%,#f5931a);overflow:hidden}
.hero-glow{position:absolute;left:60px;top:0;width:360px;height:300px;background:radial-gradient(circle at 50% 40%,var(--orange-glow) 0%,rgba(249,178,28,.55) 40%,rgba(249,178,28,0) 70%)}
.brand-name{position:absolute;left:131px;top:190px;width:222px;text-align:center;font-family:"Montserrat",sans-serif;font-weight:700;font-size:17px;line-height:21px;color:var(--white);text-transform:uppercase}
.hero-title{position:absolute;left:464px;top:52px;font-family:"Montserrat",sans-serif;font-weight:700;font-size:30px;letter-spacing:-1px;color:var(--white)}
.hero-lead{position:absolute;left:464px;top:118px;width:420px;font-family:"Montserrat",sans-serif;font-weight:500;font-size:20.5px;line-height:29px;letter-spacing:-.3px;color:var(--white)}
.skyline{position:absolute;left:0;bottom:0;width:1200px;height:70px;background:linear-gradient(180deg,rgba(17,17,17,0),rgba(17,17,17,.85) 45%,var(--ink))}
.hero-edge{position:absolute;left:0;top:344px;width:1200px;height:2px;background:#ddd}

/* content background */
.content-bg{position:absolute;left:0;top:346px;width:1200px;height:656px;background:linear-gradient(180deg,#e6e6e6,#fff 90px)}

.section-title{position:absolute;font-family:"Roboto Condensed",sans-serif;font-style:italic;font-size:19px;color:var(--heading);letter-spacing:-.3px}
.section-title span{color:#f39224}
.rule{position:absolute;height:0;border-top:1px dotted var(--rule)}
.intro{position:absolute;left:132px;width:580px;font-size:11.5px;line-height:14px;color:var(--text)}

/* quote form */
.form-label{position:absolute;font-size:11.5px;line-height:14px;color:var(--muted);text-align:right}
.field{position:absolute;width:173px;height:25px;background:var(--white);border:1px solid var(--field-border);box-shadow:inset 0 2px 3px rgba(0,0,0,.08)}
.field.select .arrow{position:absolute;right:3px;top:3px;width:16px;height:16px;border:1px solid #aaa;background:linear-gradient(#fff,#ddd)}
.message{position:absolute;left:265px;top:735px;width:418px;height:136px;background:var(--white);border:1px solid var(--field-border);box-shadow:inset 0 2px 3px rgba(0,0,0,.08)}
.pill{position:absolute;height:23px;border-radius:12px;color:var(--white);font-size:12px;display:flex;align-items:center;justify-content:center}
.pill.dark{background:linear-gradient(#4a4a4a,#000)}
.pill.bright{background:linear-gradient(#fb9a2c,var(--orange-deep))}
.submit{left:572px;top:915px;width:114px;font-weight:700;letter-spacing:.5px}

.column-divider{position:absolute;left:755px;top:433px;height:544px;border-left:1px dotted var(--rule)}

/* sidebar */
.news-title{position:absolute;font-size:12px;font-weight:700;color:var(--muted);letter-spacing:.5px}
.news-text{position:absolute;width:235px;font-size:11.5px;line-height:14px;color:var(--muted)}
.read-more{position:absolute;font-size:8px;color:#e2791c;text-decoration:underline}
.contact-details{position:absolute;left:837px;font-size:12px;line-height:14.5px;font-weight:700;color:var(--muted);letter-spacing:.6px}

/* footer */
.footer-fade{position:absolute;left:0;top:1002px;width:1200px;height:44px;background:linear-gradient(#fff,#d8d8d8)}
.footer{position:absolute;left:0;top:1046px;width:1200px;height:110px;background:linear-gradient(#2b2b2b,#111 40%,#1b1b1b);border-top:1px solid #555}
.footer ul{list-style:none;position:absolute;left:190px;top:22px;display:flex}
.footer li{height:32px;display:flex;align-items:center;font-size:10px;letter-spacing:1px;color:#ddd;text-transform:uppercase;border-left:1px solid #444}
.footer li:first-child{border-left:none}
</style>
</head>
<body>

<nav class="top-nav">
  <ul>
    <li style="width:94px">Home</li>
    <li style="width:115px">About Us</li>
    <li style="width:125px">Residential</li>
    <li style="width:113px">Commercial</li>
    <li style="width:118px">Real Estate</li>
    <li style="width:116px">Contact Us</li>
  </ul>
  <div class="search-box">
    <svg width="14" height="14" viewBox="0 0 14 14"><circle cx="8.5" cy="5.5" r="4" fill="#cfe3ee" stroke="#ddd" stroke-width="1.4"/><line x1="5.5" y1="8.5" x2="1.5" y2="12.5" stroke="#d9a441" stroke-width="2.4" stroke-linecap="round"/></svg>
    search...
  </div>
</nav>

<header class="hero">
  <div class="hero-glow" role="img" aria-label="Brand artwork glow behind the company name"></div>
  <div class="brand-name">Tall Oak Ridge<br>Property Maintenance</div>
  <h1 class="hero-title">We are Tall Oak Ridge</h1>
  <p class="hero-lead">Our goal is to connect people in search of quality property maintenance both for residential and commercial clients.</p>
  <div class="skyline" role="img" aria-label="Dark city skyline silhouette along the bottom of the banner"></div>
</header>
<div class="hero-edge"></div>

<main>
  <div class="content-bg"></div>

  <h2 class="section-title" style="left:132px;top:396px">Contact Us / Get a <span>Quote</span></h2>
  <div class="rule" style="left:132px;top:433px;width:468px"></div>

  <p class="intro" style="top:459px">Nemo enim ipsam voluptatem quia voluptas sit aspernatur aut odit aut fugit, sed quia consequuntur magni dolores eos qui ratione voluptatem sequi nesciunt.</p>
  <p class="intro" style="top:501px">Neque porro quisquam est, qui dolorem ipsum quia dolor sit amet, consectetur, adipisci velit, sed quia non numquam eius modi tempora incidunt ut labore et dolore magnam aliquam quaerat voluptatem.</p>

  <form class="quote-form">
    <label class="form-label" style="left:130px;top:580px;width:79px">First Name :</label>
    <div class="field" style="left:219px;top:574px"></div>
    <label class="form-label" style="left:420px;top:580px;width:81px">Last Name :</label>
    <div class="field" style="left:510px;top:574px"></div>

    <label class="form-label" style="left:130px;top:631px;width:79px">Email :</label>
    <div class="field" style="left:219px;top:625px"></div>
    <label class="form-label" style="left:420px;top:631px;width:81px">Address :</label>
    <div class="field" style="left:510px;top:625px"></div>

    <label class="form-label" style="left:157px;top:671px;text-align:left">Service<br>Required :</label>
    <div class="field select" style="left:219px;top:673px"><span class="arrow"><svg width="14" height="14" viewBox="0 0 14 14"><path d="M4 6h6l-3 3z" fill="#555"/></svg></span></div>
    <label class="form-label" style="left:400px;top:680px;width:102px">Company Name :</label>
    <div class="field" style="left:510px;top:673px"></div>

    <label class="form-label" style="left:159px;top:737px;text-align:left">Your message or<br>comments :</label>
    <div class="message"></div>

    <div class="pill dark submit">Get a Quote</div>
  </form>

  <div class="column-divider"></div>

  <aside>
    <h2 class="section-title" style="left:835px;top:392px;color:var(--muted)">Latest <span>News</span></h2>
    <div class="rule" style="left:833px;top:433px;width:228px"></div>

    <h3 class="news-title" style="left:835px;top:464px">Lorem ipsum doloret</h3>
    <p class="news-text" style="left:836px;top:492px">Quis autem vel eum iure reprehenderit qui in ea voluptate velit esse quam nihil mole.</p>
    <span class="read-more" style="left:1010px;top:527px">read more</span>
    <div class="rule" style="left:833px;top:565px;width:228px"></div>

    <h3 class="news-title" style="left:837px;top:592px">Lorem ipsum doloret</h3>
    <p class="news-text" style="left:838px;top:620px">Quis autem vel eum iure reprehenderit qui in ea voluptate velit esse quam nihil mole.</p>
    <span class="read-more" style="left:1012px;top:656px">read more</span>

    <h2 class="section-title" style="left:835px;top:703px;color:var(--muted)">Contact <span>Us</span></h2>
    <div class="rule" style="left:833px;top:745px;width:228px"></div>

    <p class="contact-details" style="top:777px">City Name, Australia<br>14-16 Harbourview Lane<br>Central, Sydney</p>
    <p class="contact-details" style="top:833px">tor@talloakridge.net</p>
    <p class="contact-details" style="top:861px">0800 415072<br>0800 415073</p>

    <div class="pill dark" style="left:835px;top:915px;width:59px">contact</div>
    <div class="pill bright" style="left:906px;top:915px;width:59px">quote</div>
  </aside>
</main>

<div class="footer-fade"></div>
<footer class="footer">
  <ul>
    <li style="width:115px;padding-left:28px">About Us</li>
    <li style="width:124px;justify-content:center">Residential</li>
    <li style="width:123px;justify-content:center">Commercial</li>
    <li style="width:167px;justify-content:center">Real Estate/Strata</li>
    <li style="width:163px;justify-content:center">Contact Us/Quote</li>
    <li style="width:96px;justify-content:center">Blog</li>
  </ul>
</footer>

</body>
</html>
```